依頼詳細
名刺裏面リニューアルのため、裏面のデザインをお願いいたします。
基本的にテキストのみの情報を掲載したいと思っています。
記載項目
①キャッチ
日本で唯一、新規営業に特化した営業支援会社です。

②弊社サービス紹介
・クヌーデル帳:
日本で唯一、新規営業に特化した営業ツール。
営業会社自ら、現場の声と使いやすさをもとにシステムを開発いたしました。

・企業リスト作成:
どんな営業活動も、まずはベストの営業先の見極めから。
社内、そしてWEBのデータを収集・分析を行ない、結果につながる、確度の高い企業リストを作成いたします。

・FAX集客支援:
中小企業、BtoBには非常に有効なFAXの原稿作成、またFAX配信を代行いたします。

③グループ会社一覧(社名の記載のみでかまいません)
・株式会社クレモアリス
・株式会社ミルベーナ
・ポルカノート株式会社
・株式会社ヴェルモンテ
・ハルネス株式会社
・株式会社ロザミオ
・株式会社エピフォルム
・華嶺泰股份有限公司(PELM ON RIVA CO.,LTD)
希望イメージ
シンプル 複雑
単色 カラフル
暗い 明るい
日常 高級
遊び心 厳粛
未来的 伝統的
女性的 男性的
希望する色
黒のテキストを希望します
納品ファイル
• 高解像度JPG (.jpg)
• イラストレーター形式 (.ai)
• フォトショップ形式 (.psd)
• PNG形式 (.png)
補足説明
添付にて参考までに名刺表面と既存の裏面データを送付します
当選者決定後のデータ入稿時ですが、以下の2点をお願いできますでしょうか。
------------------
①文字のアウトライン前のデータと、アウトライン済みのデータの2種類をお送
りください。
②jpg、pdfなどの見本データを一緒にお送りください。
------------------

またデザインにロゴ画像を使用していただいているご提案を当選とさせていただいた際には、
別途ロゴ画像データをお渡しいたしますので、入稿前に調整をお願いさせていただければと思います。
■ 選んだ理由

表面と並べた見たときのバランスの良さが一番のポイントとなりました。
また各コンテンツを読みやすく配置していただいており、営業の現場でもツールとして使いやすいのではないかと思ったことが選択の理由です。

■ 提案者全員のお礼・コメント

このたびは私どもの案件に多くのご提案をいただきありがとうございました。
素晴らしい提案が多く、選定に悩んでしまい、お時間をとってしまい申し訳ありませんでした。

今後もこのようなかたちでコンペを行うこともあるかと思いますが、また機会がありましたらぜひよろしくお願いいたします。

```html
<!DOCTYPE html>
<html lang="ja">
<head>
<meta charset="utf-8">
<title>名刺裏面</title>
<link rel="stylesheet" href="https://fonts.googleapis.com/css2?family=EB+Garamond:wght@400&family=Shippori+Mincho+B1:wght@400;700;800&display=swap">
<style>
  :root {
    --paper: #ffffff;
    --ink: #1a1a1a;
    --ink-soft: #2b2b2b;
  }
  * { margin: 0; padding: 0; box-sizing: border-box; }
  html, body {
    width: 831px;
    height: 1200px;
    overflow: hidden;
    background: var(--paper);
  }
  .card {
    position: relative;
    width: 831px;
    height: 1200px;
    background: var(--paper);
    color: var(--ink);
    font-family: "Shippori Mincho B1", serif;
  }
  .catch {
    position: absolute;
    top: 40px;
    right: 30px;
    writing-mode: vertical-rl;
    font-weight: 800;
    font-size: 70px;
    line-height: 1.53;
    letter-spacing: 0.02em;
    color: var(--ink);
  }
  .info {
    position: absolute;
    left: 98px;
    top: 140px;
    width: 410px;
  }
  .section-title {
    font-family: "EB Garamond", serif;
    font-weight: 400;
    font-size: 50px;
    line-height: 1;
    letter-spacing: 0.01em;
    margin-bottom: 14px;
  }
  .service { margin-bottom: 16px; }
  .service-name {
    font-weight: 700;
    font-size: 23px;
    line-height: 1.35;
  }
  .service-text {
    font-size: 21px;
    line-height: 1.48;
    color: var(--ink-soft);
    margin-bottom: 6px;
  }
  .group { margin-top: 34px; }
  .group .section-title { margin-bottom: 22px; }
  .company-list {
    list-style: none;
    font-size: 21px;
    line-height: 1.58;
    color: var(--ink-soft);
  }
  .company-list li::before { content: "・"; }
  .company-list .sub { padding-left: 21px; }
  .company-list .sub::before { content: ""; }
</style>
</head>
<body>
  <div class="card">
    <h1 class="catch">日本で唯一、新規営業に特化した<br>営業支援会社です。</h1>

    <div class="info">
      <section class="services">
        <h2 class="section-title">Service</h2>

        <div class="service">
          <h3 class="service-name">クヌーデル帳</h3>
          <p class="service-text">日本で唯一、新規営業に特化した営業ツール。</p>
          <p class="service-text">営業会社自ら、現場の声と使いやすさをもとにシステムを開発いたしました。</p>
        </div>

        <div class="service">
          <h3 class="service-name">企業リスト作成</h3>
          <p class="service-text">どんな営業活動も、まずはベストの営業先の見極めから。</p>
          <p class="service-text">社内、そしてWEBのデータを収集・分析を行ない、結果につながる、確度の高い企業リストを作成いたします。</p>
        </div>

        <div class="service">
          <h3 class="service-name">FAX集客支援</h3>
          <p class="service-text">中小企業、BtoBには非常に有効なFAXの原稿作成、またFAX配信を代行いたします。</p>
        </div>
      </section>

      <section class="group">
        <h2 class="section-title">Group company</h2>
        <ul class="company-list">
          <li>株式会社クレモアリス</li>
          <li>株式会社ミルベーナ</li>
          <li>ポルカノート株式会社</li>
          <li>株式会社ヴェルモンテ</li>
          <li>ハルネス株式会社</li>
          <li>株式会社ロザミオ</li>
          <li>株式会社エピフォルム</li>
          <li>華嶺泰股份有限公司</li>
          <li class="sub">(PELM ON RIVA CO.,LTD)</li>
        </ul>
      </section>
    </div>
  </div>
</body>
</html>
```